Help our Crumb Parlour find our winning design! We're looking for a business card....

We’re a Crumb Parlour in NY specializing in custom-made cakes and unique desserts.
Our cakes combine flavor and art, each designed to match customer’s special event and theme.
We’d like a unique business card with a clean design that will combine French chic and artistic look & feel.
We’d like to differentiate ourselves from standard bakeries, please don’t offer cupcake images :-)
Our logo is peach-pink and brown and we’d love to use these colors ( . Another color that can be added is gold - or feel free to suggest!

Target Market(s)

Women, ages 25-55

Industry/Entity Type

Boutique

Contact Information for Business Card

Text on card:
Logo
Crumb Parlour by Dana Whitfield

www.xxxxxxxx.com
xxx@xxxxx.com
(555) xxx-xxxx
F – xxxxxxxxxx
IG - xxxxxxxxx

Font styles to use
Sans Serif
Script

Requirements
Must have
• Logo
• Clean look
• French chic and artistic look & feel.
Nice to have
• Damask pattern
Should not have
• Cupcake images

```html
<!DOCTYPE html>
<html lang="en">
<head>
<meta charset="utf-8">
<title>Crumb Parlour – Business Card</title>
<link rel="stylesheet" href="https://fonts.googleapis.com/css2?family=Open+Sans:wght@400;600&display=swap">
<style>
  :root {
    --backdrop: #e9e6e3;
    --cocoa: #3b2a23;
    --peach: #f0a291;
    --peach-deep: #e48c79;
    --cream: #fbfaf8;
    --ink: #1f1a18;
    --card-w: 520px;
    --card-h: 300px;
  }
  * { box-sizing: border-box; margin: 0; padding: 0; }
  html, body { width: 1200px; height: 873px; overflow: hidden; }
  body {
    background: var(--backdrop);
    font-family: "Open Sans", Arial, sans-serif;
    display: flex;
    align-items: center;
    justify-content: center;
    gap: 48px;
  }
  .card {
    position: relative;
    width: var(--card-w);
    height: var(--card-h);
    background: var(--cocoa);
    overflow: hidden;
    box-shadow: 0 6px 18px rgba(0,0,0,.18);
  }
  .card__damask { position: absolute; inset: 0; background: var(--cocoa); }
  .card__band {
    position: absolute; top: 0; bottom: 0; left: 0; width: 38%;
    background: var(--peach);
  }
  .label-frame {
    position: absolute; left: 50%; top: 50%;
    width: 380px; height: 236px;
    transform: translate(-50%, -50%);
  }
  .label-frame svg { position: absolute; inset: 0; width: 100%; height: 100%; }
  .label-frame__content {
    position: absolute; inset: 0;
    display: flex; flex-direction: column; align-items: center; justify-content: center;
    text-align: center;
  }
  /* back */
  .brand {
    display: flex; align-items: center; gap: 8px;
    color: var(--peach-deep); font-size: 30px; font-weight: 400; letter-spacing: .5px;
  }
  .brand__dot { width: 8px; height: 8px; border-radius: 50%; background: var(--peach-deep); }
  .tagline {
    margin-top: 8px; font-size: 8px; font-weight: 600; letter-spacing: 3px;
    color: var(--cocoa); text-transform: uppercase;
  }
  /* front */
  .front__brand { font-size: 9px; color: var(--peach-deep); letter-spacing: .5px; }
  .front__name {
    margin-top: 4px; font-size: 28px; font-weight: 400; color: var(--ink);
    padding: 0 18px 4px; border-bottom: 1.5px solid var(--ink);
  }
  .contacts {
    margin-top: 14px; display: grid; grid-template-columns: repeat(3, auto);
    column-gap: 18px; row-gap: 8px; text-align: left;
  }
  .contact__label { display: block; font-size: 8px; color: var(--peach-deep); letter-spacing: .5px; }
  .contact__value { display: block; font-size: 9px; color: var(--ink); }
</style>
</head>
<body>

  <section class="card card--front">
    <div class="card__damask" role="img" aria-label="Tone-on-tone brown damask pattern"></div>
    <div class="card__band"></div>
    <div class="label-frame">
      <svg viewBox="0 0 380 236" aria-hidden="true">
        <path d="M24,0 H356 A24,24 0 0 0 380,24 V212 A24,24 0 0 0 356,236 H24 A24,24 0 0 0 0,212 V24 A24,24 0 0 0 24,0 Z" fill="var(--cream)"/>
        <path d="M30,9 H350 A22,22 0 0 0 371,30 V206 A22,22 0 0 0 350,227 H30 A22,22 0 0 0 9,206 V30 A22,22 0 0 0 30,9 Z" fill="none" stroke="var(--peach)" stroke-width="2.5"/>
      </svg>
      <div class="label-frame__content">
        <p class="front__brand">Crumb Parlour by Dana Whitfield</p>
        <h1 class="front__name">Dana Whitfield</h1>
        <div class="contacts">
          <p><span class="contact__label">Website</span><span class="contact__value">www.xxxxxxxx.com</span></p>
          <p><span class="contact__label">E-Mail</span><span class="contact__value">xxx@xxxxx.com</span></p>
          <p><span class="contact__label">Phone</span><span class="contact__value">(555) xxx-xxxx</span></p>
          <p><span class="contact__label">F</span><span class="contact__value">xxxxxxxxxx</span></p>
          <p><span class="contact__label">IG</span><span class="contact__value">xxxxxxxxx</span></p>
        </div>
      </div>
    </div>
  </section>

  <section class="card card--back">
    <div class="card__damask" role="img" aria-label="Tone-on-tone brown damask pattern"></div>
    <div class="card__band"></div>
    <div class="label-frame">
      <svg viewBox="0 0 380 236" aria-hidden="true">
        <path d="M24,0 H356 A24,24 0 0 0 380,24 V212 A24,24 0 0 0 356,236 H24 A24,24 0 0 0 0,212 V24 A24,24 0 0 0 24,0 Z" fill="var(--cream)"/>
        <path d="M30,9 H350 A22,22 0 0 0 371,30 V206 A22,22 0 0 0 350,227 H30 A22,22 0 0 0 9,206 V30 A22,22 0 0 0 30,9 Z" fill="none" stroke="var(--peach)" stroke-width="2.5"/>
      </svg>
      <div class="label-frame__content">
        <p class="brand"><span class="brand__dot"></span>Crumb Parlour</p>
        <p class="tagline">Handcrafted with love</p>
      </div>
    </div>
  </section>

</body>
</html>
```